Kestrel Meadow Greens Rollup Banner 33" X 80"

We are looking for an amazing powerful bold sexy design for a 33" X 80" roll up banner for trade shows. Text to be included on banner is attached. Initial design idea we like is is also attached. Website is www.kestrelmeadowgreens.com for more info. We like the idea of the jar underwater Blue/green effects with sun shining down through and lighting up the jar of Spirulina sitting inside the splash of water that signifies life. The quote by Odette should be highlighted near the top with graphic design of info below jar.

Target Market(s)

Health Conscious Plant Based

Industry/Entity Type

Health And Wellness

Font styles to use
Sans Serif

Colors
33a6d7
0792cd
33b8a4
87cfc6
00a990

Requirements
Must have
• Jar with Water splash
• Attached text
• Colors and font to be inline with website
• Simple beautiful clean
Nice to have
• Something sexy
Should not have
• Clutter

```html
<!DOCTYPE html>
<html lang="en">
<head>
<meta charset="utf-8">
<title>Kestrel Meadow Greens – Rollup Banners</title>
<link rel="stylesheet" href="https://fonts.googleapis.com/css2?family=Montserrat:wght@500;600;700;800&family=Roboto+Condensed:ital,wght@0,400;1,700&display=swap">
<style>
  :root {
    --page-bg: #e9eaeb;
    --teal-deep: #0b7189;
    --teal-mid: #1a9cab;
    --aqua-low: #33b8a4;
    --aqua-light: #62cbe0;
    --sky: #33a6d7;
    --ocean: #0792cd;
    --leaf: #8db33a;
    --ink: #0e1c22;
    --white: #ffffff;
  }
  * { margin: 0; padding: 0; box-sizing: border-box; }
  html, body { width: 1200px; height: 1200px; overflow: hidden; }
  body {
    background: var(--page-bg);
    position: relative;
    font-family: "Montserrat", sans-serif;
  }
  .banner-pair {
    position: absolute;
    top: 97px;
    left: 183px;
    display: flex;
    gap: 6px;
  }
  .banner {
    position: relative;
    width: 414px;
    height: 1006px;
    overflow: hidden;
    background:
      radial-gradient(ellipse 60% 35% at 50% 42%, rgba(140, 230, 240, 0.35), rgba(140, 230, 240, 0) 70%),
      linear-gradient(180deg, var(--teal-deep) 0%, var(--teal-mid) 40%, var(--teal-mid) 60%, var(--aqua-low) 72%, var(--aqua-light) 100%);
  }
  .banner__rays {
    position: absolute;
    left: 0; top: 0;
    width: 414px; height: 560px;
  }
  .brand-title {
    position: absolute;
    top: 36px;
    width: 100%;
    text-align: center;
    font-weight: 800;
    font-size: 38px;
    line-height: 43px;
    letter-spacing: 1px;
    background: linear-gradient(180deg, #f4fbff 0%, #b9e3f3 45%, var(--sky) 55%, #dff4fb 100%);
    -webkit-background-clip: text;
    background-clip: text;
    color: transparent;
  }
  .tagline {
    position: absolute;
    top: 140px;
    width: 100%;
    text-align: center;
    font-weight: 700;
    font-size: 21px;
    letter-spacing: 0.5px;
    color: var(--white);
  }
  .product-photo {
    position: absolute;
    left: 0;
    width: 414px;
  }
  .product-photo--splash {
    top: 200px; height: 336px;
    background: radial-gradient(ellipse 55% 50% at 50% 50%, #d8eef3 0%, #58b7d6 45%, rgba(26,156,171,0) 75%);
  }
  .product-photo--spoon {
    top: 236px; height: 284px;
    background: radial-gradient(ellipse 45% 45% at 55% 45%, #2a8c4c 0%, #3aa2a0 45%, rgba(26,156,171,0) 75%);
  }
  .slogan {
    position: absolute;
    top: 560px;
    width: 100%;
    text-align: center;
    font-weight: 700;
    font-size: 30px;
    color: var(--white);
  }
  .slogan__blue { color: var(--sky); }
  .slogan__green { color: var(--leaf); }
  .quote-author {
    position: absolute;
    top: 603px;
    right: 36px;
    font-weight: 600;
    font-size: 14px;
    color: var(--white);
    letter-spacing: 0.3px;
  }
  .facts {
    position: absolute;
    top: 674px;
    width: 100%;
    text-align: center;
    font-family: "Roboto Condensed", sans-serif;
    font-size: 19px;
    line-height: 27px;
    color: var(--white);
  }
  .facts strong { font-style: italic; font-weight: 700; }
  .facts__rule {
    width: 310px;
    height: 1px;
    margin: 8px auto 7px;
    background: rgba(255,255,255,0.35);
  }
  .banner__wave {
    position: absolute;
    left: 0; top: 760px;
    width: 414px; height: 80px;
  }
  .web-address {
    position: absolute;
    top: 792px;
    width: 100%;
    text-align: center;
    font-weight: 500;
    font-size: 17px;
    color: var(--ink);
    letter-spacing: 0.2px;
  }
</style>
</head>
<body>
  <main class="banner-pair">
    <section class="banner">
      <svg class="banner__rays" viewBox="0 0 414 560" aria-hidden="true">
        <defs>
          <linearGradient id="ray-fade-a" x1="0" y1="0" x2="0" y2="1">
            <stop offset="0" stop-color="#bff3f7" stop-opacity="0.25"/>
            <stop offset="1" stop-color="#bff3f7" stop-opacity="0"/>
          </linearGradient>
        </defs>
        <polygon points="150,0 190,0 240,560 120,560" fill="url(#ray-fade-a)"/>
        <polygon points="230,0 260,0 330,560 250,560" fill="url(#ray-fade-a)"/>
      </svg>
      <h1 class="brand-title">KESTREL MEADOW<br>GREENS</h1>
      <p class="tagline">A SPOONFUL OF LIFE</p>
      <div class="product-photo product-photo--splash" role="img" aria-label="Photo of a jar of green powder sitting in a splash of water"></div>
      <p class="slogan">NO <span class="slogan__blue">WATER,</span> NO <span class="slogan__green">LIFE.</span></p>
      <div class="facts">
        <p><strong>25</strong> Billion Whole Living Cells</p>
        <div class="facts__rule"></div>
        <p>Equal to <strong>1000 lbs</strong>. of Fresh Vegetables</p>
        <p><strong>ORBIS LAB 2012</strong></p>
      </div>
      <svg class="banner__wave" viewBox="0 0 414 80" aria-hidden="true">
        <path d="M0 40 C90 10 200 20 414 44" stroke="rgba(255,255,255,0.25)" stroke-width="2" fill="none"/>
      </svg>
      <p class="web-address">WWW.KESTRELMEADOWGREENS.COM</p>
    </section>

    <section class="banner">
      <svg class="banner__rays" viewBox="0 0 414 560" aria-hidden="true">
        <defs>
          <linearGradient id="ray-fade-b" x1="0" y1="0" x2="0" y2="1">
            <stop offset="0" stop-color="#bff3f7" stop-opacity="0.25"/>
            <stop offset="1" stop-color="#bff3f7" stop-opacity="0"/>
          </linearGradient>
        </defs>
        <polygon points="150,0 190,0 240,560 120,560" fill="url(#ray-fade-b)"/>
        <polygon points="230,0 260,0 330,560 250,560" fill="url(#ray-fade-b)"/>
      </svg>
      <h1 class="brand-title">KESTREL MEADOW<br>GREENS</h1>
      <p class="tagline">A SPOONFUL OF LIFE</p>
      <div class="product-photo product-photo--spoon" role="img" aria-label="Photo of a spoonful of green powder above an open jar"></div>
      <p class="slogan">NO <span class="slogan__blue">BLUE,</span> NO <span class="slogan__green">GREEN.</span></p>
      <p class="quote-author">ODETTE MARLOWE</p>
      <div class="facts">
        <p><strong>70%</strong> Raw Protein</p>
        <div class="facts__rule"></div>
        <p><strong>100%</strong> Bioavailable Full Spectrum</p>
        <p>Nutrients</p>
      </div>
      <svg class="banner__wave" viewBox="0 0 414 80" aria-hidden="true">
        <path d="M0 40 C90 10 200 20 414 44" stroke="rgba(255,255,255,0.25)" stroke-width="2" fill="none"/>
      </svg>
      <p class="web-address">WWW.KESTRELMEADOWGREENS.COM</p>
    </section>
  </main>
</body>
</html>
```